Ashcombe Prep Keystone Academy

I need a tri-fold brochure with attached information for an established private school (Ashcombe Preparatory School) based in Wellington, Florida (South Florida). We are beginning a new program (Ashcombe Prep 'Keystone' Academy) for students who are looking for a non-traditional approach to education (1 Student, 1 Teacher, Flexible Scheduling). Pictures can be altered.

Target Market(s)

Middle and High School age students and their parents

Industry/Entity Type

Education

Requirements
Must have
• Ashcombe Prep Logo...General attached information...Contact Info.

```html
<!DOCTYPE html>
<html lang="en">
<head>
<meta charset="utf-8">
<title>Ashcombe Prep Keystone Academy – Tri-fold Brochure</title>
<link rel="stylesheet" href="https://fonts.googleapis.com/css2?family=Cinzel:wght@500;600&family=Open+Sans:wght@400;600;700&display=swap">
<style>
  :root{
    --page:#e9e7e3;
    --blue:#0b5ca8;
    --blue-deep:#084a8c;
    --blue-band:#2b86d1;
    --blue-bar:#1d9bf0;
    --grey-top:#f4f4f4;
    --grey-low:#dcdde0;
    --ink:#3a3a3a;
    --navy:#123e74;
    --white:#ffffff;
  }
  *{box-sizing:border-box;margin:0;padding:0}
  html,body{width:1200px;height:907px;overflow:hidden}
  body{background:var(--page);font-family:"Open Sans",Arial,sans-serif;position:relative}
  .brochure{position:absolute;left:60px;top:70px;width:1080px;height:766px;display:flex;box-shadow:0 4px 18px rgba(0,0,0,.18)}
  .panel{position:relative;width:360px;height:766px;overflow:hidden}

  /* shared */
  .heading{position:absolute;left:0;right:0;top:352px;text-align:center;font-family:"Cinzel",Georgia,serif;font-weight:600;font-size:21px;letter-spacing:.5px}
  .web-bar{position:absolute;left:0;right:0;bottom:0;height:46px;background:linear-gradient(var(--blue-bar),#1488dd);color:var(--white);font-weight:700;font-size:14px;letter-spacing:2px;display:flex;align-items:center;justify-content:center}
  .bullets{position:absolute;list-style:none;font-size:11.5px;line-height:21.7px}
  .bullets li{position:relative;padding-left:19px}
  .bullets li::before{content:"";position:absolute;left:0;top:7px;width:7px;height:7px;border-radius:50%}

  /* panel 1 */
  .academics{background:linear-gradient(var(--blue),var(--blue-deep))}
  .academics .photo{position:absolute;left:0;top:0;width:360px;height:322px;background:linear-gradient(135deg,#cfd6dd,#8ea3b8 55%,#5c6f86)}
  .academics .band{position:absolute;left:0;right:0;top:322px;height:10px;background:var(--blue-band)}
  .academics .heading{color:var(--white)}
  .academics .copy{position:absolute;left:34px;right:30px;top:385px;color:var(--white);font-size:11.3px;line-height:15.3px;text-align:justify}
  .academics .bullets{left:36px;top:512px;color:var(--white)}
  .academics .bullets li::before{background:var(--white)}
  .academics .bullets li.two{line-height:15px;padding-top:3px;padding-bottom:4px}

  /* panel 2 */
  .endeavors{background:linear-gradient(var(--grey-top),var(--grey-low))}
  .endeavors .collage{position:absolute;left:0;top:0;width:360px;height:322px;background:var(--white)}
  .tile{position:absolute;border:2px solid var(--blue)}
  .tile.golf{left:17px;top:27px;width:89px;height:94px;background:linear-gradient(#3c7fd0,#8bb46a)}
  .tile.ski{left:17px;top:172px;width:89px;height:137px;background:linear-gradient(#4d86d2,#e8eef5)}
  .tile.feature{left:111px;top:20px;width:126px;height:292px;border:3px solid #1a1a1a;background:linear-gradient(#bfc7d1,#d87a3a 55%,#6d8fbf)}
  .tile.tennis{left:244px;top:27px;width:89px;height:133px;background:linear-gradient(#2f6fc4,#a7c2e6)}
  .tile.hoops{left:244px;top:172px;width:89px;height:137px;background:linear-gradient(#1f4f96,#3a77c6)}
  .endeavors .heading{color:var(--navy)}
  .endeavors .copy{position:absolute;left:22px;right:22px;top:385px;color:var(--ink);font-size:11.3px;line-height:15.3px;text-align:justify}
  .endeavors .bullets{top:512px;color:var(--ink)}
  .endeavors .bullets li::before{background:#222}
  .endeavors .col-a{left:25px}
  .endeavors .col-b{left:203px}
  .endeavors .fit{position:absolute;left:22px;right:22px;top:604px;color:var(--ink);font-size:11.3px;line-height:15.3px}
  .contact{position:absolute;left:86px;top:656px;color:#222;font-size:11.5px;font-weight:600;line-height:15px}
  .contact .row{display:flex;align-items:flex-start;gap:10px;margin-bottom:7px}
  .contact svg{flex:none;margin-top:1px}

  /* panel 3 */
  .cover{background:linear-gradient(var(--blue),var(--blue-deep))}
  .cover .top{position:absolute;left:0;top:0;width:360px;height:322px;background:var(--white)}
  .cover .name{position:absolute;left:0;right:0;top:46px;display:flex;align-items:center;justify-content:center;gap:10px;font-family:"Cinzel",Georgia,serif;font-weight:500;font-size:17px;line-height:22px;color:var(--navy);text-align:center}
  .cover .name .mark{width:14px;height:14px;background:var(--navy)}
  .cover .shield{position:absolute;left:0;top:0}
  .cover .headline{position:absolute;left:0;right:0;top:548px;text-align:center;color:var(--white);font-weight:700;font-size:41px;line-height:56px;letter-spacing:-.3px}
  .cover .program{position:absolute;left:0;right:0;top:664px;text-align:center;color:var(--white);font-family:"Cinzel",Georgia,serif;font-weight:500;font-size:24px;letter-spacing:.5px}
</style>
</head>
<body>
<main class="brochure">

  <section class="panel academics">
    <div class="photo" role="img" aria-label="Photo of students working together around a classroom table with laptops"></div>
    <div class="band"></div>
    <h2 class="heading">Academics</h2>
    <p class="copy">The Ashcombe Keystone Academy offers top academics in a customized setting. Students are paired with a single teacher creating the 1:1 model, which is at the core of our offering. Teachers are able to accelerate or review course material, allowing students to meet once per week while progressing through subjects at a traditional schooling pace.</p>
    <ul class="bullets">
      <li>Year Round Entry</li>
      <li>Flexible Scheduling</li>
      <li class="two">Most students meet one hour /<br>week per course</li>
      <li>Accredited Courses</li>
      <li class="two">F1 Visas (SEVIS Certified) For<br>International Students</li>
      <li>Boarding or Homestay</li>
    </ul>
    <div class="web-bar">www.ashcombeprep.org</div>
  </section>

  <section class="panel endeavors">
    <div class="collage">
      <div class="tile golf" role="img" aria-label="Photo of a golfer mid-swing"></div>
      <div class="tile ski" role="img" aria-label="Photo of a skier in snow"></div>
      <div class="tile feature" role="img" aria-label="Photo of a smiling student in a colorful striped top"></div>
      <div class="tile tennis" role="img" aria-label="Photo of a tennis player on court"></div>
      <div class="tile hoops" role="img" aria-label="Photo of a basketball player going up for a dunk"></div>
    </div>
    <h2 class="heading">Student Endeavors</h2>
    <p class="copy">Traditional schooling does not work for every student. At The Ashcombe Keystone Academy, we understand some students pursue other specialized endeavors and need a more customized academic experience. We can accommodate students irrespective of their schedule and also offer partnerships with a variety of athletic and fine arts academies including:</p>
    <ul class="bullets col-a">
      <li>Equestrian</li>
      <li>Tennis</li>
      <li>Ice Skating</li>
      <li>Basketball &amp; Baseball</li>
    </ul>
    <ul class="bullets col-b">
      <li>Golf</li>
      <li>Acting &amp; Music</li>
      <li>Many others</li>
    </ul>
    <p class="fit">Our flexible program will provide the perfect fit for your schedule.</p>
    <div class="contact">
      <div class="row">
        <svg width="10" height="14" viewBox="0 0 10 14"><path d="M5 0C2.2 0 0 2.2 0 5c0 3.6 5 9 5 9s5-5.4 5-9c0-2.8-2.2-5-5-5zm0 7a2 2 0 1 1 0-4 2 2 0 0 1 0 4z" fill="#1d8fe0"/></svg>
        <span>2480 Palm Crest Road<br>Palm Crest, Florida 33460</span>
      </div>
      <div class="row">
        <svg width="11" height="11" viewBox="0 0 24 24"><path d="M6.6 10.8a15.1 15.1 0 0 0 6.6 6.6l2.2-2.2c.3-.3.7-.4 1-.2 1.1.4 2.3.6 3.6.6.6 0 1 .4 1 1V20c0 .6-.4 1-1 1A17 17 0 0 1 3 4c0-.6.4-1 1-1h3.5c.6 0 1 .4 1 1 0 1.3.2 2.5.6 3.6.1.3 0 .7-.2 1z" fill="#1d8fe0"/></svg>
        <span>(561) 555-0142</span>
      </div>
      <div class="row">
        <svg width="10" height="10" viewBox="0 0 10 10"><circle cx="5" cy="5" r="5" fill="#1d8fe0"/></svg>
        <span>www.ashcombeprep.org</span>
      </div>
    </div>
  </section>

  <section class="panel cover">
    <div class="top"></div>
    <div class="name"><span class="mark"></span><span>Ashcombe<br>Preparatory School</span></div>
    <svg class="shield" width="360" height="766" viewBox="0 0 360 766">
      <defs>
        <linearGradient id="shieldFill" x1="0" y1="0" x2="0" y2="1">
          <stop offset="0" stop-color="#b9cfa4"/>
          <stop offset=".45" stop-color="#7fa36a"/>
          <stop offset="1" stop-color="#c9b49a"/>
        </linearGradient>
      </defs>
      <path d="M10 158 Q180 126 350 158 L350 330 Q342 468 180 540 Q18 468 10 330 Z" fill="url(#shieldFill)" stroke="#d9dde2" stroke-width="6" role="img" aria-label="Photo of a smiling student with a backpack on a leafy campus path"/>
    </svg>
    <h1 class="headline">Gret Academic<br>Starts Here</h1>
    <p class="program">Keystone Academy</p>
    <div class="web-bar">www.ashcombeprep.org</div>
  </section>

</main>
</body>
</html>
```